Morrow Engineering Core Values Branding Package

Morrow Engineering has recently refined its company Core Values and is seeking a strong, cohesive branding package to visually bring these values to life. The new graphic assets will communicate our commitment to excellence in a way that resonates with our team, clients, and partners in a blue-collar, industrial environment.

We are looking for multiple visual assets with consistent design elements that can be applied across platforms. The tone should reflect strength, reliability, and professionalism while remaining approachable and aligned with our industry.

Core Values & Descriptions
Accountability
“We take ownership of our work and actions, ensuring reliability and trust in every solution we deliver.”

Teamwork
“We collaborate across departments and disciplines to provide the highest level of service and innovation for our clients.”

Integrity
“We operate with honesty, transparency, and ethical standards in all aspects of our business.”

Growth
“We are committed to continuous improvement—of our people, our processes, and our impact in the industry.”

Deliverables

1. Primary Core Values Graphic
A master visual representing all four values together.
Designed for use on posters, office signage, internal presentations.

2. Individual Value Graphics (x4)
One graphic per core value: Accountability, Teamwork, Integrity, Growth.
Cohesive style with slight visual variation to reflect each value’s unique meaning.

Target Market(s)

Employees of Morrow Engineering

Industry/Entity Type

Blue Collar

Font styles to use
Sans Serif

Colors
0054AA
0677BA
7BADD7
CADEEF
E8F1F8
00AB8E
00BBA5
67D7C9
C6EFE9
E9F9F6
EB3D1F
EC4F4E
F09395
F8D3D4
FCEDEE

Requirements
Must have
• Accountability, Teamwork, Integrity, Growth

```html
<!DOCTYPE html>
<html lang="en">
<head>
<meta charset="UTF-8">
<title>Morrow Engineering — Core Values</title>
<link href="https://fonts.googleapis.com/css2?family=Lato:wght@400;700&family=Roboto:wght@700;900&display=swap" rel="stylesheet">
<style>
  :root {
    --navy: #003366;
    --green: #3aad2c;
    --gold: #e8b04a;
    --red: #c8102e;
    --ink: #1a1a1a;
    --paper: #ffffff;
  }
  * { margin: 0; padding: 0; box-sizing: border-box; }
  html, body { width: 954px; height: 1200px; overflow: hidden; background: var(--paper); }
  .poster { position: relative; width: 954px; height: 1200px; background: var(--paper); overflow: hidden; }
  .structure { position: absolute; inset: 0; }

  .title {
    position: absolute; left: 0; right: 0; top: 86px;
    text-align: center;
    font-family: "Roboto", sans-serif; font-weight: 900;
    font-size: 106px; line-height: 1.05; letter-spacing: -1px;
    padding-left: 4px;
  }
  .title .core { color: var(--green); }
  .title .values { color: var(--navy); }
  .site {
    position: absolute; left: 468px; width: 336px; top: 186px;
    display: flex; justify-content: space-between;
    font-family: "Lato", sans-serif; font-size: 18px; line-height: 24px; color: var(--navy);
  }

  .value { position: absolute; width: 300px; text-align: center; }
  .value .icon { width: 88px; height: 88px; margin: 0 auto 30px; border-radius: 12px; }
  .value h2 {
    font-family: "Roboto", sans-serif; font-weight: 900;
    font-size: 24.5px; line-height: 28px; margin-bottom: 22px;
  }
  .value p {
    font-family: "Lato", sans-serif; font-size: 18.5px; line-height: 21.8px; color: var(--ink);
  }
  .accountability { left: 87px; top: 495px; }
  .teamwork { left: 570px; top: 495px; }
  .integrity { left: 87px; top: 878px; }
  .growth { left: 572px; top: 878px; }
  .integrity .icon, .growth .icon { margin-bottom: 40px; }
  .accountability h2 { color: var(--navy); }
  .accountability .icon { background: var(--navy); }
  .teamwork h2 { color: var(--gold); }
  .teamwork .icon { background: var(--gold); }
  .integrity h2 { color: var(--red); }
  .integrity .icon { background: var(--red); }
  .growth h2 { color: var(--green); }
  .growth .icon { background: var(--green); }

  .seal {
    position: absolute; left: 380px; top: 717px; width: 192px; height: 192px;
    border-radius: 50%; background: var(--navy);
    display: flex; align-items: center; justify-content: center;
    font-family: "Roboto", sans-serif; font-weight: 900; font-size: 34px;
    color: var(--paper); letter-spacing: 0.5px;
  }
</style>
</head>
<body>
<main class="poster">
  <svg class="structure" width="954" height="1200" viewBox="0 0 954 1200" aria-hidden="true">
    <path class="band" fill="var(--green)" d="M0 400 C200 340 360 300 480 300 C620 300 780 350 954 400 L954 440 C780 392 620 348 480 348 C360 348 200 388 0 446 Z"/>
    <rect class="divider" x="481" y="348" width="5" height="852" fill="var(--navy)"/>
    <rect class="divider" x="0" y="810" width="954" height="5" fill="var(--navy)"/>
  </svg>

  <h1 class="title"><span class="core">CORE</span> <span class="values">VALUES</span></h1>
  <div class="site" aria-label="www.morrow-eng.example">
    <span>w</span><span>w</span><span>w</span><span>.</span><span>m</span><span>o</span><span>r</span><span>r</span><span>o</span><span>w</span><span>-</span><span>e</span><span>n</span><span>g</span><span>.</span><span>e</span><span>x</span><span>a</span><span>m</span><span>p</span><span>l</span><span>e</span>
  </div>

  <section class="value accountability">
    <div class="icon" role="img" aria-label="Icon of a worker beside a checklist with a tick"></div>
    <h2>ACCOUNTABILITY</h2>
    <p>We take ownership of our<br>work and actions, ensuring<br>reliability and trust in every<br>solution we deliver.</p>
  </section>

  <section class="value teamwork">
    <div class="icon" role="img" aria-label="Icon of four hands holding interlocking puzzle pieces"></div>
    <h2>TEAMWORK</h2>
    <p>We collaborate across<br>departments and disciplines to<br>provide the highest level of service<br>and innovation for our clients.</p>
  </section>

  <section class="value integrity">
    <div class="icon" role="img" aria-label="Icon of an open hand holding a person with a tick and an award badge"></div>
    <h2>INTEGRITY</h2>
    <p>We operate with honesty,<br>transparency, and ethical<br>standards in all aspects of<br>our business.</p>
  </section>

  <section class="value growth">
    <div class="icon" role="img" aria-label="Icon of a gear with a tick and upward arrows"></div>
    <h2>GROWTH</h2>
    <p>We are committed to<br>continuous improvement—of<br>our people, our processes, and<br>our impact in the industry.</p>
  </section>

  <div class="seal">MORROW</div>
</main>
</body>
</html>
```